Web Design Project

This is a wordpress project for a newly formed biologics company based in the US with international clientele. We do manufacturing of biologically based raw materials using a state of the art facility....Our logo must be incorporated....logo colors Navy and Gray. It is fine to use some color in web design. The viewer will primarily be industry folk.

Velstor Biologics, LLC is a contract manufacturing organization which produces biologically-based raw materials derived primarily from human plasma. The company services include extraction and purification of plasma components, especially proteins and enzymes. The business focuses on biotherapeutics, diagnostic and veterinary markets worldwide.

5 pages a bad example of first page can be found in attached files.....
use stock photos of labs and clean rooms.

Target Market(s)

target market Pharmaceutical companies and research universities

Industry/Entity Type

Veterinary

Requirements
Must have
• our logo...we will provide some graphics...

```html
<!DOCTYPE html>
<html lang="en">
<head>
<meta charset="utf-8">
<title>Velstor Biologics – Contact</title>
<link href="https://fonts.googleapis.com/css2?family=PT+Sans:wght@400;700&family=PT+Sans+Narrow:wght@400;700&display=swap" rel="stylesheet">
<style>
:root{
  --navy:#0c2a5c;
  --navy-deep:#04183a;
  --footer-top:#0d2a52;
  --footer-link:#a9b8d0;
  --footer-quick:#4f6f9c;
  --rule:#1c3a6a;
  --cyan:#6fd8e8;
  --bar:#b2b2b2;
  --field:#ffffff;
  --field-line:#c9c9c9;
  --highlight:#d6e6f7;
  --white:#ffffff;
}
*{margin:0;padding:0;box-sizing:border-box}
html,body{width:1168px;height:1200px;overflow:hidden}
body{position:relative;font-family:"PT Sans",sans-serif;
  background:linear-gradient(180deg,#d6d6d6 0,#e6e6e6 440px,#f7f7f7 700px,#cfcfcf 850px,#8f8f8f 926px)}
.abs{position:absolute}

/* header */
.site-header{left:0;top:0;width:1168px;height:87px;
  background:linear-gradient(180deg,#fbfbfb,#c9c9c9);border-bottom:2px solid var(--cyan)}
.brand{left:54px;top:16px;display:flex;align-items:center;gap:10px}
.brand-mark{width:54px;height:54px;border-radius:50%;background:var(--navy)}
.brand-name{font-weight:700;font-size:23px;color:var(--navy)}
.main-nav{left:0;top:22px;width:1168px}
.main-nav a{position:absolute;font-size:23px;color:var(--white);text-decoration:none;
  text-shadow:0 1px 2px rgba(0,0,0,.55)}
.main-nav .current{border:1px solid #9a9a9a;border-radius:8px;padding:2px 13px 6px;
  background:linear-gradient(180deg,#e4e4e4,#a8a8a8);top:2px}

/* banner */
.banner{left:30px;top:88px;width:1098px;height:246px;
  background:linear-gradient(180deg,#0b3d8a 0,#1c63bd 55%,#0a3478 100%)}
.banner-floor{left:30px;top:292px;width:1098px;height:42px;background:linear-gradient(180deg,#2a72c8,#0c2f6a)}
.slide{border:3px solid rgba(220,235,245,.8)}
.slide-side{top:122px;height:188px;background:linear-gradient(180deg,#e8eef2,#aebfcc)}
.slide-main{left:424px;top:98px;width:334px;height:226px;background:linear-gradient(180deg,#f3f7fa,#c4d4e2 70%,#3c86d6)}
.dots{left:528px;top:302px;display:flex;gap:8px}
.dots span{width:23px;height:23px;border-radius:50%;background:#1a6cc4;color:#fff;font-size:15px;
  display:flex;align-items:center;justify-content:center;border:1px solid #8fc0ee}
.dots .on{background:var(--navy-deep)}

/* page bar */
.page-bar{left:46px;top:354px;width:1050px;height:50px;background:var(--bar);border-bottom:2px solid var(--cyan)}
.page-title{left:24px;top:6px;font-family:"PT Sans Narrow",sans-serif;font-weight:700;font-size:32px;color:#fff;
  text-shadow:0 1px 2px rgba(0,0,0,.4)}
.search-box{left:826px;top:8px;width:208px;height:30px;background:#fff;border:1px solid #999;border-radius:3px;
  font-size:12px;color:#777;padding:7px 10px}
.search-box i{position:absolute;right:0;top:0;width:26px;height:28px;background:#ddd;border-left:1px solid #bbb}

/* contact info */
.info{left:78px;top:428px;width:480px;font-family:"PT Sans Narrow",sans-serif;font-size:19px;color:var(--navy);line-height:26px}
.email{left:72px;top:492px;width:232px;height:32px;background:var(--highlight);padding:3px 6px;
  font-family:"PT Sans Narrow",sans-serif;font-weight:700;font-size:20px;color:var(--navy)}
.divider{left:78px;top:534px;width:434px;border-top:2px dashed #a5a5a5}
.divider-arrow{left:520px;top:520px;color:#9a9a9a;font-size:20px;letter-spacing:2px}
.address{left:78px;top:546px;font-family:"PT Sans Narrow",sans-serif;font-size:19px;line-height:26.5px;color:var(--navy)}
.map{left:82px;top:670px;width:232px;height:190px;background:linear-gradient(160deg,#ebe7df,#dcd8cf)}
.tools{left:254px;top:868px}

/* form */
.form-title{left:668px;top:428px;font-weight:700;font-size:20px;letter-spacing:1px;color:var(--navy)}
.field-label{left:672px;font-size:20px;letter-spacing:1px;color:var(--navy)}
.field{height:27px;background:var(--field);border:1px solid var(--field-line);border-radius:3px}
.spin{right:0;top:0;width:22px;height:25px;border-left:1px solid #ddd}
.comments{left:672px;top:702px;width:364px;height:102px;background:#fff;border:1px solid var(--field-line);border-radius:8px}
.btn{top:812px;height:25px;border:1px solid #a8a8a8;border-radius:3px;background:linear-gradient(#f4f4f4,#d2d2d2);
  font-size:14px;color:#555;text-align:center;line-height:23px}

/* footer */
.site-footer{left:0;top:926px;width:1168px;height:274px;background:linear-gradient(180deg,var(--footer-top),var(--navy-deep))}
.col{top:58px;font-size:21px;line-height:26.4px}
.col-main{color:var(--footer-link)}
.col-quick{color:var(--footer-quick)}
.col-rule{top:28px;width:2px;height:176px;background:var(--rule)}
.follow{left:956px;top:48px;font-size:21px;color:var(--footer-quick)}
.social{top:84px;width:28px;height:28px;border-radius:3px;background:#5a8fd0}
.foot-search{left:956px;top:136px;width:158px;height:28px;background:#164486;border-bottom:2px solid #6a86b0;
  color:#fff;font-size:15px;font-weight:700;padding:4px 10px}
.foot-search i{position:absolute;right:0;top:0;width:20px;height:26px;background:#7f93b3}
.copyright{left:0;top:232px;width:1168px;text-align:center;font-size:12px;color:#2d4f86}
</style>
</head>
<body>

<header class="site-header abs">
  <div class="brand abs"><span class="brand-mark"></span><span class="brand-name">Velstor Biologics</span></div>
  <nav class="main-nav abs">
    <a style="left:512px">Home</a>
    <a style="left:608px">Facilities</a>
    <a style="left:734px">Team</a>
    <a style="left:824px">Announcements</a>
    <a class="current" style="left:1024px">Contact</a>
  </nav>
</header>

<section class="banner abs"></section>
<div class="banner-floor abs"></div>
<div class="slide slide-side abs" style="left:270px;width:180px" role="img" aria-label="Laboratory bench photo"></div>
<div class="slide slide-side abs" style="left:758px;width:220px" role="img" aria-label="Clean room equipment photo"></div>
<div class="slide slide-main abs" role="img" aria-label="Clean room corridor photo"></div>
<div class="dots abs"><span>1</span><span>2</span><span class="on">3</span><span>4</span></div>

<div class="page-bar abs">
  <h1 class="page-title abs">Contact</h1>
  <div class="search-box abs">Search<i></i></div>
</div>

<p class="info abs">Should you wish to contact us via email, please click the following link, or complete the form below.</p>
<div class="email abs">jdorran@velstorbio.com</div>
<div class="divider abs"></div>
<div class="divider-arrow abs">&gt;&gt;</div>
<address class="address abs" style="font-style:normal">Adress<br>418 Marrowind Rd* Unit 201<br>Calverton, Oregon<br>USA</address>
<div class="map abs" role="img" aria-label="Street map showing the company location"></div>
<svg class="tools abs" width="56" height="26" viewBox="0 0 56 26">
  <g fill="#fff" stroke="#666" stroke-width="1.2">
    <rect x="6" y="2" width="14" height="8"/><rect x="2" y="9" width="22" height="10" rx="2"/><rect x="6" y="15" width="14" height="9"/>
    <rect x="30" y="5" width="24" height="17"/><path d="M30 5 L42 15 L54 5" fill="none"/>
  </g>
</svg>

<h2 class="form-title abs">Contact Details</h2>
<div class="field-label abs" style="top:476px">Name</div>
<div class="field abs" style="left:738px;top:478px;width:302px"></div>
<div class="field-label abs" style="top:515px">City</div>
<div class="field abs" style="left:738px;top:517px;width:302px"></div>
<div class="field-label abs" style="top:554px">State</div>
<div class="field abs" style="left:738px;top:556px;width:302px"></div>
<div class="field-label abs" style="top:593px">Country</div>
<div class="field abs" style="left:766px;top:595px;width:274px"><span class="spin abs"></span></div>
<div class="field-label abs" style="top:632px">Phone</div>
<div class="field abs" style="left:746px;top:634px;width:294px"></div>
<div class="field-label abs" style="top:671px">Comments</div>
<div class="comments abs"></div>
<div class="btn abs" style="left:828px;width:98px">Send Details</div>
<div class="btn abs" style="left:936px;width:98px">Clear Details</div>

<footer class="site-footer abs">
  <div class="col col-main abs" style="left:74px">Home<br>Facilities<br>Team<br>Links<br>Contact</div>
  <div class="col-rule abs" style="left:215px"></div>
  <div class="col col-quick abs" style="left:260px">Some Quick Links<br>Some Quick Links<br>Some Quick Links<br>Some Quick Links<br>Some Quick Links</div>
  <div class="col-rule abs" style="left:463px"></div>
  <div class="col col-quick abs" style="left:490px">Some Quick Links<br>Some Quick Links<br>Some Quick Links<br>Some Quick Links<br>Some Quick Links</div>
  <div class="col-rule abs" style="left:695px"></div>
  <div class="col col-quick abs" style="left:728px">Some Quick Links<br>Some Quick Links<br>Some Quick Links<br>Some Quick Links<br>Some Quick Links</div>
  <div class="col-rule abs" style="left:923px"></div>
  <div class="follow abs">Follow us</div>
  <span class="social abs" style="left:958px"></span>
  <span class="social abs" style="left:998px"></span>
  <div class="foot-search abs">Search<i></i></div>
  <p class="copyright abs">Copyright ©201 Velstor Biologics</p>
</footer>

</body>
</html>
```